Northway Trade Partners Needs a FRESH website

We would like a creative minded designer to take on the task to Re-design our website. Its a simple 5-7 pages. With no cart, no complex html. Just plain information about our company and products we import and export. Pictures added to the product section. Since Our logo its Blue, we would like the designer to use complementing colors in order to make the website look cleaner and modern.

Target Market(s)

The target audience will be companies looking to purchase plastic related products. Companies looking to purchase large quantities of plastic containers (Shampoo bottles, caps, sprayers, mist sprayers, cosmetic containers etc).

Industry/Entity Type

It Company

Font styles to use
Sans Serif

Requirements
Must have
• We have a section in which we would like to add pictures of some of the products we carry, therefore having an easy and clean way to navigate through the pictures will be a plus.

```html
<!DOCTYPE html>
<html lang="en">
<head>
<meta charset="utf-8">
<title>Northway Trade Partners</title>
<link href="https://fonts.googleapis.com/css2?family=Open+Sans:ital,wght@0,400;0,600;1,400&family=Lora:ital,wght@0,400;1,400;1,700&display=swap" rel="stylesheet">
<style>
:root{
  --brand:#0a9fdb;
  --brand-dark:#0788c2;
  --brand-text:#1a87c4;
  --heading-blue:#0d6fb0;
  --accent-red:#c0141f;
  --soft-red:#e24b4b;
  --body:#7d7d7d;
  --dark-body:#555;
  --rule:#dcdcdc;
  --footer:#3b3b3b;
  --white:#fff;
}
*{margin:0;padding:0;box-sizing:border-box}
html,body{width:736px;height:1200px;overflow:hidden;background:var(--white)}
body{position:relative;font-family:"Open Sans",Arial,sans-serif;color:var(--body)}
.abs{position:absolute}

/* header */
.site-header{left:0;top:0;width:736px;height:52px;background:var(--brand)}
.brand{left:80px;top:8px;display:flex;align-items:center;gap:6px}
.brand-mark{width:36px;height:36px;border-radius:50%;background:var(--brand-dark)}
.brand-name{font-size:8px;font-weight:600;color:var(--white);width:70px;line-height:1.2}
.main-nav{left:302px;top:0;height:52px;display:flex}
.main-nav a{display:block;height:52px;line-height:52px;font-family:"Lora",Georgia,serif;font-style:italic;font-size:8.5px;color:var(--white);text-decoration:none;padding:0 11px}
.main-nav a.active{background:var(--brand-dark);padding:0 12px}

/* hero */
.hero{left:0;top:52px;width:736px;height:411px;background:linear-gradient(90deg,#8cc4ec 0%,#d8ebf8 25%,#f4f9fd 50%,#d8ebf8 75%,#7fb9e6 100%)}
.slider{left:78px;top:74px;width:580px;height:350px;background:var(--white);padding:3px;box-shadow:0 2px 10px rgba(0,0,0,.25)}
.slide-photo{width:100%;height:100%;background:radial-gradient(circle at 50% 50%,#f4f4f4 0%,#e5e1dd 55%,#d9cfc7 100%)}
.slide-title{left:78px;top:249px;width:580px;text-align:center;font-family:"Lora",Georgia,serif;font-style:italic;font-weight:700;font-size:19px;color:var(--heading-blue)}
.slide-arrow{top:231px;width:34px;height:34px}

/* quote */
.quote-band{left:0;top:463px;width:736px;height:40px;background:linear-gradient(#ececec,#fff)}
.quote-mark{top:472px;font-family:Georgia,serif;font-size:44px;color:#9a9a9a;line-height:1}
.quote-text{left:120px;top:482px;width:496px;text-align:center;font-family:"Lora",Georgia,serif;font-size:12.6px;line-height:19px;color:var(--brand-text);white-space:nowrap}
.quote-name{left:0;top:527px;width:736px;text-align:center;font-size:8.5px;font-style:italic;color:var(--dark-body)}
.rule{left:79px;width:575px;height:1px;background:var(--rule)}

/* welcome */
.section-title{font-family:"Lora",Georgia,serif;font-style:italic;font-weight:700}
.welcome-title{left:79px;top:577px;font-size:16px;color:var(--accent-red)}
.welcome-copy{left:79px;top:602px;width:320px;font-size:8.1px;line-height:16px;color:var(--body);white-space:nowrap}
.welcome-copy p{margin-bottom:8px}
.btn{display:block;background:var(--brand-dark);color:var(--white);text-decoration:none;text-align:center;box-shadow:0 1px 2px rgba(0,0,0,.3)}
.btn-read{left:80px;top:749px;width:71px;height:23px;line-height:23px;font-size:9px}
.welcome-photo{left:419px;top:597px;width:235px;height:178px;background:radial-gradient(ellipse at 50% 60%,#f2f6fb 0%,#d8e6f5 45%,#3f6fb3 100%)}

/* columns */
.col-title{top:826px;font-size:12.5px;color:var(--heading-blue)}
.divider{top:853px;width:1px;height:228px;background:var(--rule)}
.about-photo{left:79px;top:854px;width:167px;height:110px;border:2px solid #eee;background:linear-gradient(135deg,#e9e4dc 0%,#d9353a 35%,#2fa84a 60%,#f1c40f 80%,#5a4a8a 100%)}
.about-lead{left:79px;top:973px;width:180px;font-family:"Lora",Georgia,serif;font-style:italic;font-size:9.3px;line-height:14px;color:var(--soft-red);white-space:nowrap}
.about-copy{left:79px;top:1007px;width:175px;font-size:6.4px;line-height:14.4px;color:var(--dark-body);white-space:nowrap}
.about-copy a{color:var(--brand-dark);text-decoration:none;font-size:8px}

.news-item{left:302px;width:172px;height:60px}
.news-thumb{position:absolute;left:0;top:0;width:55px;height:55px;border:2px solid #e6e6e6}
.news-title{position:absolute;left:66px;top:2px;font-family:"Lora",Georgia,serif;font-style:italic;font-size:7.5px;color:var(--accent-red);white-space:nowrap}
.news-text{position:absolute;left:66px;top:16px;width:108px;font-size:6.4px;line-height:12px;color:var(--dark-body);white-space:nowrap}
.news-date{position:absolute;left:67px;top:44px;font-size:6.4px;color:var(--heading-blue)}
.news-more{position:absolute;left:138px;top:44px;font-size:6.4px;color:var(--brand-dark);text-decoration:underline}
.news-sep{left:302px;width:172px;border-top:1px dashed #ccc}
.btn-small{top:1089px;width:52px;height:16px;line-height:16px;font-size:7.5px}

.market{left:523px;width:132px;height:78px}
.market-name{position:absolute;left:0;top:0;font-family:"Lora",Georgia,serif;font-style:italic;font-size:9.5px;color:var(--accent-red)}
.market-text{position:absolute;left:1px;top:16px;width:95px;font-size:6.6px;line-height:13.2px;color:var(--body);white-space:nowrap}
.market-text a{color:var(--heading-blue);font-style:italic;font-weight:600}
.market-icon{position:absolute;left:97px;top:12px;width:38px;height:38px}
.market-sep{left:521px;width:134px;border-top:1px dashed #ccc}

/* footer */
.site-footer{left:0;top:1135px;width:736px;height:65px;background:var(--footer)}
.footer-nav{left:81px;top:1153px;font-size:8px;color:var(--white)}
.footer-nav a{color:var(--white);text-decoration:none}
.copyright{left:81px;top:1175px;font-size:6.8px;color:#a9a9a9}
.social{left:572px;top:1159px;display:flex;gap:6px}
.social span{width:17px;height:17px;border-radius:50%;background:var(--white)}
</style>
</head>
<body>

<header class="site-header abs">
  <div class="brand abs"><span class="brand-mark"></span><span class="brand-name">Northway Trade Partners</span></div>
  <nav class="main-nav abs">
    <a class="active" href="#">HOME</a>
    <a href="#">PRODUCTS</a>
    <a href="#" style="padding-left:20px">MISSION STATEMENT</a>
    <a href="#">ABOUT US</a>
    <a href="#">CONTACT US</a>
  </nav>
</header>

<section class="hero abs"></section>
<div class="slider abs"><div class="slide-photo" role="img" aria-label="Hands holding piles of coloured plastic pellets arranged in a circle"></div></div>
<div class="slide-title abs">Global Market Strategy</div>
<svg class="slide-arrow abs" style="left:80px" viewBox="0 0 34 34" aria-hidden="true"><circle cx="17" cy="17" r="15" fill="none" stroke="#fff" stroke-width="2" opacity=".6"/><path d="M20 9 L12 17 L20 25" fill="none" stroke="#fff" stroke-width="2" opacity=".6"/></svg>
<svg class="slide-arrow abs" style="left:615px" viewBox="0 0 34 34" aria-hidden="true"><circle cx="17" cy="17" r="15" fill="none" stroke="#fff" stroke-width="2"/><path d="M13 9 L22 17 L13 25 Z" fill="#fff"/></svg>

<div class="quote-band abs"></div>
<div class="quote-mark abs" style="left:101px">“</div>
<div class="quote-mark abs" style="left:605px">”</div>
<p class="quote-text abs">Neque porro quisquam est qui dolorem ipsum quia dolor sit amet consectetu<br>velitncvbxLorem ipsum dolor sit ametconsectetur adipisicing elit</p>
<p class="quote-name abs">Name, City Name</p>
<div class="rule abs" style="top:552px"></div>

<h1 class="section-title welcome-title abs">Welcome To Our Comapny</h1>
<div class="welcome-copy abs">
  <p>Lorem ipsum dolor sit amet, consectetur adipisicing elit, sed do eiusmod tempor<br>ut labore et dolore magna aliqua. Ut enim ad minim veniam, quis nostrud exercit<br>co laboris nisi ut aliquip ex ea commodo consequat. Duis aute irure dolor in repre<br>henderit involuptate velit esse cillum dolore eu.</p>
  <p>Lorem ipsum dolor sit amet, consectetur adipisicing elit, sed do eiusmod tempor<br>ut labore et dolore magna aliqua. Ut enim ad minim veniam, quis nostrud exercit<br>co laboris nisi ut aliquip ex ea commodo consequat. Duis aute irure dolor in repre<br>henderit involuptate velit esse cillum dolore eu.</p>
</div>
<a class="btn btn-read abs" href="#">Read More</a>
<div class="welcome-photo abs" role="img" aria-label="Heap of clear white plastic pellets on a blue surface"></div>
<div class="rule abs" style="top:797px"></div>

<h2 class="section-title col-title abs" style="left:80px">About our Company</h2>
<h2 class="section-title col-title abs" style="left:302px">News</h2>
<h2 class="section-title col-title abs" style="left:521px">Markets We Serve</h2>
<div class="divider abs" style="left:274px"></div>
<div class="divider abs" style="left:498px"></div>

<div class="about-photo abs" role="img" aria-label="Bands of red, green, yellow, black and purple plastic granules"></div>
<p class="about-lead abs">Ut scelerisque vehicula nfisl, in vemass<br>vehicula quis. Duis felis ante.</p>
<p class="about-copy abs">Lorem ipsum dolor sit amt ut labet, consectetur axdi<br>ng elit, sed do eiusmod tempojhdfhgsfr incididunt ut<br>re et dolore magna aliqua. Ut et ut labnim ad mincim<br>am, quis nostrud exercitation ullamt ut labco laboris<br>Lorem ipsum dolor sit amet, const ut labectetur xadi<br>am, quis nostrud exercitation ullamct ut labo laboris n<br>ut aliquip ex ea commodo consequat. <a href="#">Read More</a></p>

<div class="news-item abs" style="top:854px">
  <div class="news-thumb" role="img" aria-label="White plastic pellets" style="background:radial-gradient(#f4f7fb,#9fb7d6)"></div>
  <p class="news-title">Ut scelerisque vehicullorem jg</p>
  <p class="news-text">Lorem ipsum dolor sit ametcfghfn<br>ng elit, sed do eius.</p>
  <span class="news-date">03.23.13</span><a class="news-more" href="#">Read More</a>
</div>
<div class="news-sep abs" style="top:919px"></div>
<div class="news-item abs" style="top:932px">
  <div class="news-thumb" role="img" aria-label="Soft blue abstract light" style="background:linear-gradient(135deg,#cfe6f8,#fff 50%,#9dcbef)"></div>
  <p class="news-title">Ut scelerisque vehicullorem jg</p>
  <p class="news-text">Lorem ipsum dolor sit ametcfghfn<br>ng elit, sed do eius.</p>
  <span class="news-date">03.23.13</span><a class="news-more" href="#">Read More</a>
</div>
<div class="news-sep abs" style="top:997px"></div>
<div class="news-item abs" style="top:1011px">
  <div class="news-thumb" role="img" aria-label="Colourful plastic cups" style="background:linear-gradient(135deg,#f0a3c8,#e33c3c 45%,#7ad0e6)"></div>
  <p class="news-title">Ut scelerisque vehicullorem jg</p>
  <p class="news-text">Lorem ipsum dolor sit ametcfghfn<br>ng elit, sed do eius.</p>
  <span class="news-date">03.23.13</span><a class="news-more" href="#">Read More</a>
</div>
<div class="news-sep abs" style="top:1076px"></div>
<a class="btn btn-small abs" style="left:302px" href="#">View More</a>

<div class="market abs" style="top:851px">
  <p class="market-name">Bottle</p>
  <p class="market-text">Converters of PET bottles,<br>containers and preforms<br>have truste. <a href="#">Read more »</a></p>
  <svg class="market-icon" viewBox="0 0 38 38" aria-hidden="true"><circle cx="19" cy="19" r="18" fill="#e9e9e9"/><rect x="15.5" y="13" width="7" height="15" rx="2" fill="#1a87c4"/><rect x="17" y="9" width="4" height="4" fill="#1a87c4"/></svg>
</div>
<div class="market-sep abs" style="top:917px"></div>
<div class="market abs" style="top:929px">
  <p class="market-name">Sheet</p>
  <p class="market-text">Converters of PET bottles,<br>containers and preforms<br>have truste. <a href="#">Read more »</a></p>
  <svg class="market-icon" viewBox="0 0 38 38" aria-hidden="true"><circle cx="19" cy="19" r="18" fill="#e9e9e9"/><path d="M9 18 L19 13 L29 18 L19 23 Z" fill="#1a87c4"/><path d="M9 21 L19 26 L29 21" fill="none" stroke="#1a87c4" stroke-width="1.5"/><path d="M9 24 L19 29 L29 24" fill="none" stroke="#1a87c4" stroke-width="1.5"/></svg>
</div>
<div class="market-sep abs" style="top:995px"></div>
<div class="market abs" style="top:1008px">
  <p class="market-name">Fibeer</p>
  <p class="market-text">Converters of PET bottles,<br>containers and preforms<br>have truste. <a href="#">Read more »</a></p>
  <svg class="market-icon" viewBox="0 0 38 38" aria-hidden="true"><circle cx="19" cy="19" r="18" fill="#e9e9e9"/><path d="M8 16 Q19 10 30 18 L26 27 Q17 20 10 24 Z" fill="#4aa6d8"/></svg>
</div>
<div class="market-sep abs" style="top:1074px"></div>
<a class="btn btn-small abs" style="left:525px" href="#">View More</a>

<footer class="site-footer abs"></footer>
<nav class="footer-nav abs"><a href="#">Home</a> &nbsp;| &nbsp;<a href="#">Products</a> | <a href="#">Mission Statement</a> | <a href="#">About Us</a> &nbsp;| <a href="#">Contact Us</a></nav>
<p class="copyright abs">© 2014. All rights reserved</p>
<div class="social abs" aria-hidden="true"><span></span><span></span><span></span><span></span></div>

</body>
</html>
```